Business Card Design - Carrington Hill Lodge

We are looking at a new design for our business cards that has a modern and professional look. We run a residential aged care facility focussing on the care of residents. The cards will be used for potential clients, consultants and business opportunities in this sector. Blue and white is our main colours and would to see these colours incorporated in the design.
Industry/Entity Type
Business
Contact Information for Business Card
Carrington Hill Lodge, Darren Pelham, dpelham@carringtonhilllodge.com.au, Finance Manager, 0491 736 208, BCom, 48 Yarrabee Way, Bellbrook Park, Qld 4109.

```html
<!DOCTYPE html>
<html lang="en">
<head>
<meta charset="utf-8">
<title>Carrington Hill Lodge – Business Cards</title>
<link rel="stylesheet" href="https://fonts.googleapis.com/css2?family=Tinos&display=swap">
<style>
  :root {
    --backdrop: #e6e6e8;
    --card-light: #eef4f9;
    --card-mid: #bcd1e1;
    --card-back: #8fbad8;
    --ink: #2f5f80;
    --brand: #4a7892;
    --taupe: #a89a8f;
    --on-taupe: #f4f1ee;
    --badge: #2f6a8c;
  }
  * { margin: 0; padding: 0; box-sizing: border-box; }
  html, body { width: 1200px; height: 800px; overflow: hidden; }
  body {
    background: var(--backdrop);
    font-family: "Tinos", "Times New Roman", serif;
    position: relative;
  }
  .card {
    position: absolute;
    border-radius: 4px;
    box-shadow: 0 10px 22px rgba(0,0,0,.18);
  }
  .card--front {
    left: 70px; top: 90px; width: 520px; height: 300px;
    background: radial-gradient(ellipse at 35% 35%, var(--card-light) 0%, var(--card-mid) 100%);
  }
  .card--back {
    left: 600px; top: 400px; width: 540px; height: 310px;
    background: radial-gradient(ellipse at 25% 50%, var(--card-light) 0%, var(--card-back) 75%);
  }
  .brand {
    position: absolute;
    text-align: center;
    color: var(--brand);
  }
  .brand__mark {
    display: block;
    width: 70px; height: 70px;
    border-radius: 50%;
    background: var(--brand);
    margin: 0 auto 14px;
  }
  .brand__name {
    display: block;
    font-size: 32px;
    letter-spacing: 2px;
    text-transform: uppercase;
    line-height: 1.1;
    white-space: nowrap;
  }
  .brand__tagline {
    display: inline-block;
    font-size: 17px;
    color: var(--on-taupe);
    background: var(--taupe);
    padding: 3px 18px;
    margin-top: 8px;
    letter-spacing: .5px;
  }
  .card--front .brand { left: 0; right: 0; top: 76px; }
  .card--back .brand { left: 20px; width: 270px; top: 70px; }
  .card--back .brand__mark { width: 54px; height: 54px; margin-bottom: 10px; }
  .card--back .brand__name { font-size: 18px; letter-spacing: 1px; }
  .card--back .brand__tagline { font-size: 12px; padding: 2px 12px; margin-top: 6px; }
  .partner-badge {
    position: absolute; left: 80px; top: 245px;
    width: 150px; height: 26px; border-radius: 13px;
    background: var(--badge);
  }
  .contact {
    position: absolute; left: 310px; top: 34px;
    color: var(--ink);
  }
  .contact__name { font-size: 24px; line-height: 1; }
  .contact__role { font-size: 12px; margin-bottom: 14px; }
  .contact__phone { font-size: 17px; margin-bottom: 4px; }
  .contact__line { font-size: 12px; line-height: 1.35; }
  .contact__address { font-size: 15px; margin-top: 16px; line-height: 1.3; }
  .registry-badge {
    position: absolute; left: 310px; top: 230px;
    width: 180px; height: 40px;
    border-top: 1px solid var(--ink);
    display: flex; align-items: center; gap: 10px; padding-top: 6px;
  }
  .registry-badge__shape {
    width: 34px; height: 30px; border-radius: 4px; background: var(--ink); opacity: .75;
  }
  .registry-badge__bar {
    flex: 1; height: 14px; border-radius: 3px; background: var(--ink); opacity: .5;
  }
</style>
</head>
<body>
  <section class="card card--front">
    <div class="brand">
      <span class="brand__mark"></span>
      <span class="brand__name">Carrington Hill Lodge</span>
      <span class="brand__tagline">Comfort, Respect, Belonging</span>
    </div>
  </section>

  <section class="card card--back">
    <div class="brand">
      <span class="brand__mark"></span>
      <span class="brand__name">Carrington Hill Lodge</span>
      <span class="brand__tagline">Comfort, Respect, Belonging</span>
    </div>
    <div class="partner-badge" role="img" aria-label="Partner service badge"></div>

    <div class="contact">
      <p class="contact__name">Darren Pelham</p>
      <p class="contact__role">Finance Manager</p>
      <p class="contact__phone">0491 736 208</p>
      <p class="contact__line">dpelham@carringtonhilllodge.com.au</p>
      <p class="contact__line">carringtonhilllodge.com.au</p>
      <p class="contact__address">48 Yarrabee Way,<br>Bellbrook Park, Qld 4109</p>
    </div>
    <div class="registry-badge" role="img" aria-label="Government accreditation badge">
      <span class="registry-badge__shape"></span>
      <span class="registry-badge__bar"></span>
    </div>
  </section>
</body>
</html>
```